Packaging design for a revolutionary hi-protein snack of Norwegian salmon

We need a breathtaking packing design for a smal snack bag (30 g) for a revolutionary new hi-protein snack made of Norwegian salmon. The product will be made with two different flavors; MANGO and WASABI. The product is extreme high in protein (60%) and omega 3, and are just natural.

We want to see a bold and fresh design that appeals to protein lovers of all ages.

Target Market(s)

Our target market is boys and girls that are 18-35 years old and that are interested in working out and eating healthy.

Industry/Entity Type

Snack industry (functional food, healthy snack, protein snack)

Font styles to use
Sans Serif

Requirements
Must have
• The package design must give the customer a WOW feeling. "HI-PROTEIN SNACK" must be highligted. Further, the design must use the Tidal Compass setup (attached).

```html
<!DOCTYPE html>
<html lang="en">
<head>
<meta charset="utf-8">
<title>Fjordbite Hi-protein Snack – Mango</title>
<link href="https://fonts.googleapis.com/css2?family=Anton&family=Oswald:wght@600;700&family=Poppins:wght@700;800&display=swap" rel="stylesheet">
<style>
  :root {
    --backdrop: #e9ebee;
    --ocean-deep: #0f4fae;
    --ocean: #1f6fcf;
    --ocean-light: #4aa3e6;
    --kelp: #5f9e25;
    --kelp-light: #b9dc80;
    --mango: #e6a02a;
    --ink-blue: #1a45a3;
    --shadow-blue: #0a3a8c;
    --shadow-green: #2f5f10;
    --salmon: #e8662a;
    --salmon-light: #f39a5c;
    --salmon-dark: #c94d1c;
    --white: #ffffff;
  }
  * { margin: 0; padding: 0; box-sizing: border-box; }
  html, body { width: 1200px; height: 1117px; overflow: hidden; }
  body { background: var(--backdrop); position: relative; font-family: "Poppins", sans-serif; }

  .pouch {
    position: absolute; left: 289px; top: 97px; width: 632px; height: 900px;
    border-radius: 26px 26px 14px 14px; overflow: hidden;
    background: linear-gradient(180deg, var(--ocean-light) 0%, var(--ocean) 45%, var(--ocean-deep) 100%);
  }
  .pouch-art { position: absolute; inset: 0; }

  .brand {
    position: absolute; left: 339px; top: 122px; width: 194px; text-align: center;
    font-family: "Poppins", sans-serif; font-weight: 800; font-size: 56px; line-height: 0.98;
    color: var(--white);
  }

  .natural-badge { position: absolute; left: 64px; top: 178px; display: flex; align-items: center; gap: 12px; }
  .natural-badge__ring { width: 64px; height: 64px; border: 3px solid var(--white); border-radius: 50%; display: grid; place-items: center; }
  .natural-badge__text { color: var(--white); font-weight: 800; line-height: 0.95; }
  .natural-badge__pct { font-size: 34px; display: block; }
  .natural-badge__word { font-size: 19px; display: block; }

  .headline { position: absolute; text-align: center; color: var(--white); font-family: "Anton", sans-serif; white-space: nowrap; }
  .headline--top { left: 170px; width: 390px; top: 246px; font-size: 94px; line-height: 1.1; text-shadow: 0 5px 0 var(--shadow-blue), 3px 5px 0 var(--shadow-blue); letter-spacing: -1px; }
  .headline--main { left: 66px; width: 486px; top: 330px; font-size: 206px; line-height: 1; text-shadow: 0 8px 0 var(--shadow-blue), 6px 8px 0 var(--shadow-blue); letter-spacing: -3px; }

  .origin {
    position: absolute; left: 232px; top: 556px; width: 180px; text-align: center;
    font-family: "Oswald", sans-serif; font-weight: 600; font-size: 36px; line-height: 1.02;
    color: var(--white); text-shadow: 0 2px 0 var(--shadow-green);
  }

  .flavour {
    position: absolute; left: 175px; top: 682px; width: 236px; height: 97px;
    background: var(--mango); border-radius: 48px;
    display: flex; align-items: center; padding-left: 24px;
    font-weight: 800; font-size: 52px; color: var(--ink-blue);
  }

  .salmon-photo { position: absolute; left: 392px; top: 434px; width: 245px; height: 360px; }

  .claim { position: absolute; left: 58px; width: 110px; text-align: center; color: var(--white); font-weight: 700; font-size: 15px; line-height: 1.15; list-style: none; }
  .claim--carbs { top: 576px; }
  .claim--protein { top: 658px; }
  .claim--omega { top: 740px; }
  .claim__tick { width: 24px; height: 24px; border-radius: 50%; background: var(--mango); display: grid; place-items: center; margin: 0 auto 8px; }

  .weight { position: absolute; left: 64px; top: 826px; width: 100px; text-align: center; color: var(--white); font-weight: 800; font-size: 38px; line-height: 1; }

  .benefit { position: absolute; top: 800px; width: 96px; text-align: center; color: var(--white); font-weight: 700; font-size: 11px; line-height: 1.2; list-style: none; }
  .benefit--muscle { left: 172px; }
  .benefit--heart { left: 264px; }
  .benefit--slim { left: 359px; }
  .benefit__icon { width: 38px; height: 38px; border: 2px solid var(--mango); border-radius: 50%; margin: 0 auto 8px; display: grid; place-items: center; }
  .benefit--slim .benefit__label { display: block; padding-top: 6px; }

  .origin-seal { position: absolute; left: 486px; top: 800px; width: 84px; height: 70px; border: 2px solid rgba(255,255,255,0.85); border-radius: 6px; }
</style>
</head>
<body>
<main class="pouch">
  <svg class="pouch-art" viewBox="0 0 632 900" aria-hidden="true">
    <defs>
      <linearGradient id="kelpShine" x1="0" y1="0" x2="0.6" y2="1">
        <stop offset="0" stop-color="var(--kelp-light)" stop-opacity="0.9"/>
        <stop offset="0.5" stop-color="var(--kelp-light)" stop-opacity="0.2"/>
        <stop offset="1" stop-color="var(--kelp-light)" stop-opacity="0"/>
      </linearGradient>
    </defs>
    <path d="M0 0 H104 C200 150 330 330 455 520 C470 600 450 700 420 770 H205 C140 600 60 420 0 300 Z" fill="var(--kelp)"/>
    <path d="M0 0 H104 C200 150 330 330 455 520 C470 600 450 700 420 770 H205 C140 600 60 420 0 300 Z" fill="url(#kelpShine)"/>
  </svg>

  <div class="brand">Fjord<br>bite</div>

  <div class="natural-badge">
    <span class="natural-badge__ring">
      <svg width="34" height="34" viewBox="0 0 34 34" fill="none" stroke="#fff" stroke-width="2.4" stroke-linecap="round"><path d="M17 31V16"/><path d="M17 20c-6 0-10-4-10-9 6 0 10 4 10 9z"/><path d="M17 16c0-6 4-10 10-10 0 6-4 10-10 10z"/></svg>
    </span>
    <span class="natural-badge__text"><span class="natural-badge__pct">100%</span><span class="natural-badge__word">NATURAL</span></span>
  </div>

  <h1 class="headline headline--top">Hi-protein</h1>
  <div class="headline headline--main">Snack</div>

  <p class="origin">Made of norwegian salmon</p>

  <div class="flavour">Mango</div>

  <svg class="salmon-photo" viewBox="0 0 245 360" role="img" aria-label="Photo of a piece of dried salmon jerky">
    <defs>
      <linearGradient id="salmonTone" x1="0" y1="0" x2="1" y2="1">
        <stop offset="0" stop-color="var(--salmon-light)"/>
        <stop offset="0.6" stop-color="var(--salmon)"/>
        <stop offset="1" stop-color="var(--salmon-dark)"/>
      </linearGradient>
    </defs>
    <path d="M210 0 C235 25 245 90 245 160 L245 300 C235 330 200 350 165 356 C120 340 60 320 20 290 C0 270 0 250 20 230 C60 190 110 150 150 120 C175 90 195 40 210 0 Z" fill="url(#salmonTone)"/>
  </svg>

  <ul>
    <li class="claim claim--carbs"><span class="claim__tick"><svg width="14" height="14" viewBox="0 0 14 14"><path d="M2 7l3.5 3.5L12 3.5" fill="none" stroke="#1a45a3" stroke-width="2.4"/></svg></span>LOW IN<br>CARBS 2%</li>
    <li class="claim claim--protein"><span class="claim__tick"><svg width="14" height="14" viewBox="0 0 14 14"><path d="M2 7l3.5 3.5L12 3.5" fill="none" stroke="#1a45a3" stroke-width="2.4"/></svg></span>PROTEIN<br>60%</li>
    <li class="claim claim--omega"><span class="claim__tick"><svg width="14" height="14" viewBox="0 0 14 14"><path d="M2 7l3.5 3.5L12 3.5" fill="none" stroke="#1a45a3" stroke-width="2.4"/></svg></span>HIGH IN<br>OMEGA 3</li>
  </ul>

  <div class="weight">30 g</div>

  <ul>
    <li class="benefit benefit--muscle"><span class="benefit__icon"><svg width="20" height="20" viewBox="0 0 20 20" fill="none" stroke="#e6a02a" stroke-width="1.8"><path d="M3 15c3-1 5-4 6-8l3-2 2 3-3 1c1 3 3 4 5 4"/></svg></span>MUSCLE<br>BUILDING</li>
    <li class="benefit benefit--heart"><span class="benefit__icon"><svg width="20" height="20" viewBox="0 0 20 20" fill="none" stroke="#e6a02a" stroke-width="1.8"><path d="M10 17S3 12 3 7a3.5 3.5 0 0 1 7-1 3.5 3.5 0 0 1 7 1c0 5-7 10-7 10z"/><path d="M5 10h3l1-2 2 4 1-2h3"/></svg></span>BETTER HEART<br>HEALTH</li>
    <li class="benefit benefit--slim"><span class="benefit__icon"><svg width="20" height="20" viewBox="0 0 20 20" fill="none" stroke="#e6a02a" stroke-width="1.8"><path d="M6 3c1 5 1 9-1 14M14 3c-1 5-1 9 1 14M8 10h4"/></svg></span><span class="benefit__label">SLIMMING</span></li>
  </ul>

  <div class="origin-seal" aria-hidden="true"></div>
</main>
</body>
</html>
```